Letterhead design for Dental Practice - Ashby Lane Dental Care

Letterhead for Private Dental Practice. To be used for all official correspondance and for printing treatment details on to be given to patients.

Target Market(s)

Private dental patients

Industry/Entity Type

Dental Clinic

Font styles to use
Other font styles liked:
• nexa-light

Colors
33a6d7
1c66ac
85abd2

Requirements
Must have
• info in the footer and header needs to be 3.5cm from upper/lower boader of paper, see photo in uploaded files
• info details:
• tel. 0115 947 3051
• email info@ashbylanedc.co.uk
• ashbylanedentalcare.co.uk
• 17b Ashby Lane Elmfield Harwick HX4 7QT
• nexa-light font as in uploaded logo files
Should not have
• No funny tooth pictures

```html
<!DOCTYPE html>
<html lang="en">
<head>
<meta charset="utf-8">
<title>Ashby Lane Dental Care – Letterhead</title>
<link rel="stylesheet" href="https://fonts.googleapis.com/css2?family=Quicksand:wght@400;500&display=swap">
<style>
  :root {
    --backdrop: #d6d6d6;
    --paper: #ffffff;
    --brand-blue: #33a6d7;
    --band-blue: #139fd9;
    --soft-blue: #85abd2;
    --rule-blue: #9fd3ec;
    --ink-grey: #555a5e;
  }
  * { box-sizing: border-box; margin: 0; padding: 0; }
  html, body {
    width: 1200px;
    height: 1000px;
    overflow: hidden;
    background: var(--backdrop);
    font-family: "Quicksand", sans-serif;
  }
  .letterhead {
    position: absolute;
    left: 275px;
    top: 40px;
    width: 650px;
    height: 920px;
    background: var(--paper);
    box-shadow: 0 4px 14px rgba(0,0,0,0.18);
    overflow: hidden;
  }
  .letterhead__header {
    position: absolute;
    top: 62px;
    left: 0;
    right: 0;
    display: flex;
    flex-direction: column;
    align-items: center;
    gap: 14px;
  }
  .brand-mark {
    width: 34px;
    height: 34px;
    border-radius: 50%;
    background: var(--brand-blue);
  }
  .brand-name {
    font-weight: 400;
    font-size: 27px;
    letter-spacing: 0.5px;
    color: var(--brand-blue);
    white-space: nowrap;
  }
  .letterhead__rule {
    position: absolute;
    top: 158px;
    left: 38px;
    right: 38px;
    height: 1px;
    background: var(--rule-blue);
  }
  .letterhead__footer {
    position: absolute;
    left: 44px;
    bottom: 62px;
  }
  .contact-list {
    list-style: none;
    display: flex;
    flex-direction: column;
    gap: 20px;
  }
  .contact-item {
    display: flex;
    align-items: center;
    gap: 6px;
    font-size: 13px;
    font-weight: 500;
    color: var(--ink-grey);
    white-space: nowrap;
  }
  .contact-icon { width: 14px; height: 14px; flex: none; }
  .postal-address {
    margin-top: 18px;
    font-size: 15px;
    font-weight: 500;
    color: var(--brand-blue);
    font-style: normal;
    white-space: nowrap;
  }
  .corner-disc {
    position: absolute;
    right: 58px;
    bottom: 40px;
    width: 72px;
    height: 72px;
    border-radius: 50%;
    border: 6px solid var(--soft-blue);
  }
  .footer-band {
    position: absolute;
    left: 0;
    bottom: 0;
    width: 420px;
    height: 20px;
  }
</style>
</head>
<body>
  <main class="letterhead">
    <header class="letterhead__header">
      <span class="brand-mark" aria-hidden="true"></span>
      <span class="brand-name">Ashby Lane Dental Care</span>
    </header>
    <div class="letterhead__rule"></div>

    <footer class="letterhead__footer">
      <ul class="contact-list">
        <li class="contact-item">
          <svg class="contact-icon" viewBox="0 0 14 14" aria-hidden="true">
            <circle cx="7" cy="7" r="6" fill="none" stroke="var(--brand-blue)" stroke-width="1.5"/>
            <path d="M5 4.2 L6 6 L5.4 6.6 Q6.4 8.2 7.6 8.8 L8.2 8.2 L9.8 9 L9.2 10 Q6.2 9.8 4.2 5.2 Z" fill="var(--brand-blue)"/>
          </svg>
          <span>0115 947 3051</span>
        </li>
        <li class="contact-item">
          <svg class="contact-icon" viewBox="0 0 14 14" aria-hidden="true">
            <circle cx="7" cy="7" r="6" fill="none" stroke="var(--brand-blue)" stroke-width="1.5"/>
            <rect x="4" y="5" width="6" height="4.2" fill="var(--brand-blue)"/>
            <path d="M4 5 L7 7.4 L10 5" fill="none" stroke="#fff" stroke-width="0.8"/>
          </svg>
          <span>info@ashbylanedc.co.uk</span>
        </li>
        <li class="contact-item">
          <svg class="contact-icon" viewBox="0 0 14 14" aria-hidden="true">
            <circle cx="7" cy="7" r="6" fill="none" stroke="var(--brand-blue)" stroke-width="1.5"/>
            <circle cx="7" cy="7" r="3" fill="none" stroke="var(--brand-blue)" stroke-width="1"/>
            <path d="M4 7 H10 M7 4 V10" stroke="var(--brand-blue)" stroke-width="0.8"/>
          </svg>
          <span>ashbylanedentalcare.co.uk</span>
        </li>
      </ul>
      <address class="postal-address">17b Ashby Lane Elmfield Harwick HX4 7QT</address>
    </footer>

    <span class="corner-disc" aria-hidden="true"></span>

    <svg class="footer-band" viewBox="0 0 420 20" preserveAspectRatio="none" aria-hidden="true">
      <polygon points="0,0 420,0 408,20 0,20" fill="var(--band-blue)"/>
    </svg>
  </main>
</body>
</html>
```